Real Estate Business Cards

Looking for a clean, sharp and professional look for our Real Estate investment Fund that invests in Multi Family Apartment buildings.

Target Market(s)

Real Estate Fund

Industry/Entity Type

Real Estate

Contact Information for Business Card

Company Description: Real Estate Investment Fund
Company Name: RKW Holdings
Name: Marcus Olvane
Cell: (917) 482-0657
Email: marcus@rkwholdings-example.com
Website: www.rkwholdings-example.com
Address: 418, 9th Street, Brooklyn NY 11218

Colors

Designer to choose colors to be used in the design.

Requirements
Nice to have
• Colors to match logo

```html
<!DOCTYPE html>
<html lang="en">
<head>
<meta charset="utf-8">
<title>RKW Holdings – Business Cards</title>
<link href="https://fonts.googleapis.com/css2?family=Cinzel:wght@400;500&family=Poppins:wght@300;400&display=swap" rel="stylesheet">
<style>
  :root{
    --brand-blue:#1a6fa8;
    --brand-blue-deep:#135b8c;
    --charcoal:#3c3d40;
    --paper:#ffffff;
    --backdrop:#c9cacc;
    --text-dark:#3a3a3c;
  }
  *{box-sizing:border-box;margin:0;padding:0}
  html,body{width:1200px;height:801px;overflow:hidden}
  body{
    background:var(--backdrop);
    display:flex;align-items:center;justify-content:center;gap:40px;
    font-family:"Poppins",sans-serif;
  }
  .card{
    position:relative;width:540px;height:309px;overflow:hidden;
    box-shadow:0 6px 18px rgba(0,0,0,.18);
  }
  .card__art{position:absolute;inset:0;width:100%;height:100%;display:block}

  .brand{
    position:absolute;display:flex;align-items:center;gap:9px;
    font-family:"Cinzel",serif;font-weight:400;color:var(--text-dark);
    letter-spacing:.04em;white-space:nowrap;
  }
  .brand__mark{width:12px;height:12px;background:var(--brand-blue);flex:none}

  /* Front */
  .card--front{background:var(--brand-blue)}
  .card--front .brand{left:276px;right:0;top:72px;justify-content:center;font-size:24px}
  .contact{position:absolute;left:34px;bottom:28px;color:var(--paper)}
  .contact__name{
    font-family:"Cinzel",serif;font-weight:500;font-size:20px;
    letter-spacing:.05em;margin-bottom:8px;white-space:nowrap;
  }
  .contact__address{font-size:11.5px;line-height:1.35;font-weight:300;margin-bottom:8px}
  .contact__list{list-style:none;font-size:11.5px;font-weight:300;line-height:1.45}
  .contact__list li{display:flex;align-items:center;gap:8px;white-space:nowrap}
  .contact__icon{width:10px;height:10px;flex:none}

  /* Back */
  .card--back{background:var(--paper)}
  .pattern-field{
    position:absolute;left:0;bottom:0;width:200px;height:160px;
    border-top-right-radius:20px;
    background:linear-gradient(135deg,var(--brand-blue) 0%,var(--brand-blue-deep) 55%,var(--charcoal) 100%);
  }
  .card--back .brand{right:34px;top:176px;font-size:28px}
  .card--back .website{
    position:absolute;right:34px;top:220px;font-size:11px;
    letter-spacing:.2em;color:var(--text-dark);font-weight:400;white-space:nowrap;
  }
</style>
</head>
<body>

  <section class="card card--front" aria-label="Business card front">
    <svg class="card__art" viewBox="0 0 540 309" aria-hidden="true">
      <path d="M241 0 V197 Q241 209 253 209 H540" fill="none" stroke="var(--charcoal)" stroke-width="14"/>
      <path d="M255 0 V185 Q255 195 265 195 H540" fill="none" stroke="var(--paper)" stroke-width="14"/>
      <path d="M269 0 V173 Q269 181 277 181 H540" fill="none" stroke="var(--charcoal)" stroke-width="14"/>
      <path d="M276 0 H540 V174 H284 Q276 174 276 166 Z" fill="var(--paper)"/>
    </svg>

    <div class="brand"><span class="brand__mark"></span>RKW Holdings</div>

    <div class="contact">
      <p class="contact__name">Marcus Olvane</p>
      <p class="contact__address">418, 9th Street<br>Brooklyn NY 11218</p>
      <ul class="contact__list">
        <li>
          <svg class="contact__icon" viewBox="0 0 10 10"><rect x="2" y="0.5" width="6" height="9" rx="1" fill="none" stroke="#fff" stroke-width="1.2"/></svg>
          (917) 482-0657
        </li>
        <li>
          <svg class="contact__icon" viewBox="0 0 10 10"><rect x="0.5" y="2" width="9" height="6.5" fill="#fff"/><path d="M0.5 2 L5 5.8 L9.5 2" fill="none" stroke="var(--brand-blue)" stroke-width="1"/></svg>
          marcus@rkwholdings-example.com
        </li>
        <li>
          <svg class="contact__icon" viewBox="0 0 10 10"><circle cx="5" cy="5" r="4.4" fill="none" stroke="#fff" stroke-width="1.1"/><ellipse cx="5" cy="5" rx="1.8" ry="4.4" fill="none" stroke="#fff" stroke-width="0.9"/><path d="M0.6 5 H9.4" stroke="#fff" stroke-width="0.9"/></svg>
          www.rkwholdings-example.com
        </li>
      </ul>
    </div>
  </section>

  <section class="card card--back" aria-label="Business card back">
    <div class="pattern-field" role="img" aria-label="Large decorative brand pattern in blue and charcoal"></div>
    <div class="brand"><span class="brand__mark"></span>RKW Holdings</div>
    <p class="website">www.rkwholdings-example.com</p>
  </section>

</body>
</html>
```